New business card design

I need original, modern, business looking but dzen (minimalistic) looking design.
Also refer to websit trevanix.ru

Text is

Дробышев Кирилл, PMP
Партнер

Моб. +7 (915) 460 7185
info@trevanix.ru
Москва, Россия, 117342, ул. Береговая 7/2
=====================

Drobyshev Kirill, PMP
Partner

Mob. +7 (915) 460 7185
info@trevanix.ru
Moscow, Russia,117342, Beregovaya 7/2

Industry/Entity Type

Business

Font styles to use
Serif
Sans Serif

```html
<!DOCTYPE html>
<html lang="en">
<head>
<meta charset="utf-8">
<title>Trevanix — Business Card</title>
<link rel="stylesheet" href="https://fonts.googleapis.com/css2?family=Open+Sans:wght@300;400;600&display=swap">
<style>
  :root {
    --canvas-bg: #d9d9d9;
    --card-bg: #f7f7f5;
    --brand-blue: #1a7cc1;
    --brand-teal: #3aa6c9;
    --ink: #2b2b2b;
    --ink-soft: #6d6d6d;
    --mark-grey: #8a8a8a;
    --white: #ffffff;
  }
  * { box-sizing: border-box; margin: 0; padding: 0; }
  html, body { width: 1200px; height: 1200px; overflow: hidden; }
  body {
    background: var(--canvas-bg);
    font-family: "Open Sans", Arial, sans-serif;
    color: var(--ink);
    position: relative;
  }
  .card {
    position: absolute;
    left: 150px;
    width: 900px;
    height: 500px;
    background: var(--card-bg);
    box-shadow: 0 6px 18px rgba(0,0,0,0.18);
    overflow: hidden;
  }
  .card--front { top: 50px; }
  .card--back { top: 650px; }

  .brand {
    position: absolute;
    display: flex;
    align-items: center;
    gap: 22px;
  }
  .brand__square {
    width: 64px;
    height: 64px;
    background: var(--brand-teal);
  }
  .brand__name {
    font-weight: 300;
    font-size: 84px;
    line-height: 1;
    color: var(--brand-blue);
    letter-spacing: -1px;
  }
  .card--front .brand { left: 230px; top: 150px; }
  .card--back .brand { left: 50px; top: 45px; }

  .brand--small { gap: 8px; }
  .brand--small .brand__square { width: 18px; height: 18px; background: var(--mark-grey); }
  .brand--small .brand__name { font-size: 22px; font-weight: 400; color: var(--mark-grey); letter-spacing: 0; }

  .band {
    position: absolute;
    height: 30px;
    background: var(--brand-blue);
    color: var(--white);
    font-size: 18px;
    line-height: 30px;
    text-align: center;
  }
  .card--front .band { left: 0; right: 0; top: 385px; }
  .card--front .brand--small { right: 22px; top: 430px; }

  .card--back .band { left: 0; width: 700px; top: 420px; }
  .card--back .brand--small { left: 718px; top: 423px; }

  .person { position: absolute; left: 55px; top: 240px; }
  .person__name { font-size: 17px; color: var(--ink-soft); }
  .person__role { font-size: 21px; font-weight: 600; color: var(--brand-blue); margin-top: 2px; }

  .contacts {
    position: absolute;
    left: 470px;
    top: 315px;
    font-size: 16px;
    line-height: 1.5;
    color: var(--ink);
    list-style: none;
  }
</style>
</head>
<body>
  <section class="card card--front">
    <div class="brand">
      <span class="brand__square"></span>
      <span class="brand__name">Trevanix</span>
    </div>
    <div class="band">trevanix.ru</div>
    <div class="brand brand--small">
      <span class="brand__square"></span>
      <span class="brand__name">Trevanix</span>
    </div>
  </section>

  <section class="card card--back">
    <div class="brand">
      <span class="brand__square"></span>
      <span class="brand__name">Trevanix</span>
    </div>
    <div class="person">
      <p class="person__name">Drobyshev Kirill, PMP</p>
      <p class="person__role">Partner</p>
    </div>
    <ul class="contacts">
      <li>Mob. +7 (915) 460 7185</li>
      <li>info@trevanix.ru</li>
      <li>Moscow, Russia,117342, Beregovaya 7/2</li>
    </ul>
    <div class="band"></div>
    <div class="brand brand--small">
      <span class="brand__square"></span>
      <span class="brand__name">Trevanix</span>
    </div>
  </section>
</body>
</html>
```